Velmo Corporate Website for technological company

We need a modern website to promote our product and services.
You can found the actually website at the address: www.velmo-example.ch

We are a new company for B2B market. We would like do show our high precision and innovation capability.

we need a section were is possible to easily upload "news" and documents for our customers.

Target Market(s)

B2B services in the industry market

Industry/Entity Type

It Company

Coding

Coded - Design and coding required

Number of Pages Required

5+ page

Font styles to use
Other font styles liked:
• We accept propositions

Requirements
Must have
• Easy to maintain
• Presentation of the Velmo company
• Presentation of Velmo services and products
• The customer can download our ducumentation
Nice to have
• Sexy and modern

```html
<!DOCTYPE html>
<html lang="en">
<head>
<meta charset="utf-8">
<title>Velmo Sagl – Precision Systems</title>
<link href="https://fonts.googleapis.com/css2?family=Montserrat:wght@400;600;700;800&family=Open+Sans:wght@400;600;700&display=swap" rel="stylesheet">
<style>
:root{
  --olive:#a29a5a;
  --olive-dark:#857d42;
  --ink:#141414;
  --text:#333;
  --muted:#8a8a8a;
  --line:#e2e2e2;
  --panel:#f1f1f1;
  --white:#fff;
  --sale:#d8232a;
  --star:#f0b400;
}
*{box-sizing:border-box;margin:0;padding:0}
html,body{width:1200px;height:3488px;overflow:hidden}
body{font-family:"Open Sans",Arial,sans-serif;color:var(--text);background:var(--white);position:relative}
.abs{position:absolute}
h1,h2,h3,h4{font-family:"Montserrat",Arial,sans-serif}

/* header */
.topbar{top:0;left:0;width:1200px;height:48px}
.topbar ul{list-style:none;display:flex;gap:28px;position:absolute;left:440px;top:16px;font-size:11px;font-weight:600;text-transform:uppercase;color:var(--ink);align-items:center}
.topbar svg{vertical-align:middle;margin:0 4px}
.brand{left:60px;top:34px;display:flex;align-items:center;gap:14px}
.brand .mark{width:44px;height:44px;background:var(--olive)}
.brand .name{font-family:"Montserrat",sans-serif;font-weight:800;font-size:40px;color:var(--ink);letter-spacing:1px}
.search{left:440px;top:70px;width:540px;height:40px;display:flex;border:1px solid var(--line)}
.search .field{flex:1;padding:10px 14px;font-size:13px;color:var(--muted)}
.search .cat{width:200px;border-left:1px solid var(--line);padding:10px 14px;font-size:13px;color:var(--muted);display:flex;justify-content:space-between}
.search .go{width:48px;background:var(--olive);display:flex;align-items:center;justify-content:center}
.cart{left:1020px;top:78px;font-size:15px;color:var(--ink);display:flex;align-items:center;gap:10px}
.cart .count{position:absolute;left:100px;top:-8px;width:18px;height:18px;border-radius:50%;background:var(--olive);color:#fff;font-size:10px;text-align:center;line-height:18px}
.nav{top:144px;left:0;width:1200px;height:40px;background:var(--olive)}
.nav ul{list-style:none;display:flex;position:absolute;left:228px;top:0;height:40px}
.nav li{font-family:"Montserrat",sans-serif;font-weight:600;font-size:13px;color:#fff;padding:0 24px;line-height:40px;text-transform:uppercase}
.nav li.active{background:var(--ink)}

/* hero */
.hero{top:188px;left:0;width:1200px;height:444px;
  background:
    radial-gradient(ellipse 520px 200px at 620px 400px,rgba(230,140,60,.55),rgba(230,140,60,0) 70%),
    radial-gradient(ellipse 360px 180px at 180px 160px,rgba(40,40,44,.75),rgba(40,40,44,0) 70%),
    linear-gradient(180deg,#b9c6d3 0%,#d6dce2 34%,#a4a29c 62%,#5c4c3c 86%,#3a302a 100%)}
.hero h1{position:absolute;right:60px;top:150px;text-align:right;font-size:40px;line-height:52px;font-weight:700;color:#1c2430;text-transform:uppercase;letter-spacing:1px}
.btn{display:inline-block;background:var(--olive);color:#fff;font-family:"Montserrat",sans-serif;font-weight:600;font-size:14px;padding:0 22px;line-height:44px;white-space:nowrap}
.hero .btn{position:absolute;right:60px;top:268px}

/* promos */
.promos{top:632px;left:0;width:1200px;height:368px;background:var(--panel)}
.promo{position:absolute;top:68px;height:252px}
.promo.a{left:60px;width:320px;background:radial-gradient(ellipse at 35% 40%,#9fb0c0,#4f5860 70%,#2e3338)}
.promo.b{left:432px;width:328px;background:radial-gradient(ellipse at 55% 55%,#2a2a2a 0,#4a4a4a 22%,#dcdcdc 48%,#f4f4f4 80%)}
.promo.c{left:788px;width:352px;background:radial-gradient(ellipse at 70% 60%,#c9c4b4,#6a6a6a 60%,#3e3e3e)}
.promo h3{position:absolute;color:#fff;font-size:26px;font-weight:700;text-transform:uppercase;white-space:nowrap}
.promo.a h3{right:24px;top:140px}
.promo.a .btn{position:absolute;right:24px;top:190px;line-height:36px;font-size:13px}
.promo.c h3{left:24px;top:18px}
.promo.c .btn{position:absolute;left:24px;top:68px;line-height:36px;font-size:13px}

/* products */
.featured{top:1000px;left:0;width:1200px;height:1032px;background:var(--panel)}
.featured h2{position:absolute;top:48px;width:1200px;text-align:center;font-size:40px;font-weight:700;color:var(--ink);text-transform:uppercase}
.card{position:absolute;width:252px;height:380px;background:var(--white)}
.card .title{position:absolute;left:14px;top:12px;font-size:14px;font-weight:700;color:var(--ink)}
.card .price{position:absolute;left:14px;top:34px;font-size:12px;font-weight:700;color:var(--ink)}
.card .price s{color:var(--muted);font-weight:400;margin-right:4px}
.card .stars{position:absolute;left:14px;top:54px;color:var(--star);font-size:12px;letter-spacing:1px}
.card .photo{position:absolute;left:26px;top:84px;width:200px;height:210px}
.card .zoom{position:absolute;right:12px;top:88px;width:24px;height:24px;background:var(--ink);display:flex;align-items:center;justify-content:center}
.card .sale{position:absolute;right:12px;top:58px;background:var(--sale);color:#fff;font-size:9px;font-weight:700;padding:3px 6px}
.card .btn{position:absolute;left:62px;top:318px;width:128px;text-align:center;line-height:38px;font-size:13px;padding:0}

/* why band */
.why{top:2032px;left:0;width:1200px;height:480px;overflow:hidden}
.why .photo{position:absolute;left:0;top:0;width:620px;height:480px;background:radial-gradient(circle at 38% 52%,#e6e6e6 0,#a8a8a8 22%,#5a5a5a 48%,#2f2f2f 78%)}
.why .panel{position:absolute;left:440px;top:0;width:760px;height:480px;background:linear-gradient(90deg,rgba(150,142,80,0) 0,rgba(150,142,80,.85) 14%,var(--olive) 24%,#8f8848 60%,var(--olive-dark))}
.why h2{position:absolute;left:580px;top:96px;color:#fff;font-size:28px;line-height:38px;font-weight:700;text-transform:uppercase;white-space:nowrap}
.why ul{position:absolute;left:580px;top:212px;width:560px;list-style:none;color:#fff;font-size:13px;line-height:26px}
.why li::before{content:"✓";margin-right:10px;font-weight:700}
.why .btn{position:absolute;left:580px;top:356px;background:var(--ink);line-height:42px}

/* get started */
.start{top:2512px;left:0;width:1200px;height:520px}
.start h2{position:absolute;top:100px;width:1200px;text-align:center;font-size:34px;font-weight:700;color:var(--ink)}
.start .sub{position:absolute;top:154px;width:1200px;text-align:center;font-size:14px;color:var(--text)}
.step{position:absolute;top:236px;width:104px;height:104px;border-radius:50%;background:var(--olive);display:flex;align-items:center;justify-content:center}
.start .dots{position:absolute;top:286px;left:352px;width:496px;border-top:4px dotted var(--ink)}
.signup{position:absolute;top:404px;left:320px;display:flex}
.signup .field{width:452px;height:40px;border:1px solid #cfcfcf}
.signup .go{width:108px;height:40px;background:var(--ink);color:#fff;font-weight:600;font-size:14px;text-align:center;line-height:40px}

/* perks strip */
.perks{top:3032px;left:0;width:1200px;height:96px;display:flex}
.perk{flex:1;display:flex;align-items:center;justify-content:center;gap:16px;color:#fff}
.perk.dark{background:var(--ink)}
.perk.olive{background:var(--olive)}
.perk .t{font-family:"Montserrat",sans-serif;font-weight:700;font-size:17px;text-transform:uppercase}
.perk .s{font-size:12px}

/* footer */
.footer{top:3128px;left:0;width:1200px;height:320px}
.col{position:absolute;top:70px}
.col h4{font-size:17px;font-weight:700;color:var(--ink);text-transform:uppercase;margin-bottom:18px}
.col p,.col li{font-size:12px;line-height:22px;color:var(--text);list-style:none}
.col li::before{content:"› ";color:var(--olive)}
.pay{display:flex;gap:8px;margin-bottom:18px}
.pay span{width:40px;height:24px;border-radius:3px;background:#d7d7d7}
.col .label{font-size:11px;font-weight:700;color:var(--ink);text-transform:uppercase;margin-bottom:10px}
.news{width:240px}
.news .field{display:flex;width:240px;height:32px;border:1px solid #cfcfcf;margin-top:12px}
.news .field i{flex:1;font-size:11px;color:var(--muted);padding:8px;font-style:normal}
.news .field b{width:34px;background:var(--olive)}
.social{display:flex;gap:10px;margin-top:16px}
.social span{width:22px;height:22px;border-radius:50%;background:#cfcfcf}
.legal{top:3448px;left:0;width:1200px;height:40px;border-top:1px solid var(--line);font-size:11px;color:var(--muted)}
.legal .left{position:absolute;left:60px;top:13px}
.legal .right{position:absolute;right:60px;top:13px;display:flex;gap:26px}
</style>
</head>
<body>

<header>
  <div class="abs topbar">
    <ul>
      <li>Call us now <svg width="14" height="14" viewBox="0 0 24 24"><path fill="#a29a5a" d="M6.6 10.8a15 15 0 0 0 6.6 6.6l2.2-2.2c.3-.3.7-.4 1-.2 1.1.4 2.3.6 3.6.6.6 0 1 .4 1 1V20c0 .6-.4 1-1 1A17 17 0 0 1 3 4c0-.6.4-1 1-1h3.5c.6 0 1 .4 1 1 0 1.3.2 2.5.6 3.6.1.3 0 .7-.2 1z"/></svg> +41 (0)00 555 01 23</li>
      <li>Cash on delivery</li>
      <li>Free delivery</li>
      <li>Free exchanges</li>
    </ul>
  </div>
  <div class="abs brand"><span class="mark"></span><span class="name">VELMO Sagl</span></div>
  <div class="abs search">
    <div class="field">Search</div>
    <div class="cat">All Categories <span>▾</span></div>
    <div class="go"><svg width="18" height="18" viewBox="0 0 24 24"><circle cx="10" cy="10" r="6.5" fill="none" stroke="#fff" stroke-width="2.5"/><path d="M15 15l6 6" stroke="#fff" stroke-width="2.5"/></svg></div>
  </div>
  <div class="abs cart">My Cart
    <svg width="28" height="26" viewBox="0 0 24 22"><path d="M1 2h4l3 12h12l2-9H6" fill="none" stroke="#141414" stroke-width="2"/><circle cx="9" cy="18" r="2" fill="#141414"/><circle cx="19" cy="18" r="2" fill="#141414"/></svg>
    <span class="count">0</span>
  </div>
  <nav class="abs nav">
    <ul>
      <li class="active">Home</li><li>Services</li><li>Products</li><li>Examples</li><li>Downloads</li><li>Contact</li>
    </ul>
  </nav>
</header>

<section class="abs hero" role="img" aria-label="City skyline at dusk with glowing lights and two control units in the foreground">
  <h1>Simulation and modeling of<br>complete processes</h1>
  <span class="btn">Buy Here Now</span>
</section>

<section class="abs promos">
  <div class="promo a" role="img" aria-label="Engineer working at a lab test bench"><h3>Buy Valuepacks</h3><span class="btn">Buy Now</span></div>
  <div class="promo b" role="img" aria-label="Precision gear drive module on a light background"></div>
  <div class="promo c" role="img" aria-label="Technician assembling an industrial machine"><h3>Buy Valuepacks</h3><span class="btn">Buy Now</span></div>
</section>

<section class="abs featured">
  <h2>Featured Products</h2>

  <article class="card" style="left:60px;top:140px"><span class="title">Products Velmo 1</span><span class="price"><s>$130.00</s>$110.00</span><span class="stars">★★★★★</span><span class="sale">SALE</span><div class="photo" role="img" aria-label="Electric starter motor" style="background:radial-gradient(ellipse at 50% 55%,#8d8d8d,#c8c8c8 45%,#fff 75%)"></div><span class="zoom"><svg width="12" height="12" viewBox="0 0 24 24"><circle cx="10" cy="10" r="6" fill="none" stroke="#fff" stroke-width="3"/><path d="M15 15l6 6" stroke="#fff" stroke-width="3"/></svg></span><span class="btn">Add to Cart</span></article>
  <article class="card" style="left:336px;top:140px"><span class="title">Products Velmo 2</span><span class="price"><s>$130.00</s>$110.00</span><span class="stars">★★★★★</span><div class="photo" role="img" aria-label="Servo motor with gearbox" style="background:radial-gradient(ellipse at 50% 55%,#7a806c,#c9cbc0 45%,#fff 75%)"></div><span class="btn">Add to Cart</span></article>
  <article class="card" style="left:612px;top:140px"><span class="title">Products Velmo 3</span><span class="price"><s>$130.00</s>$110.00</span><span class="stars">★★★★★</span><div class="photo" role="img" aria-label="Compact DC motor" style="background:radial-gradient(ellipse at 50% 50%,#a88a5a,#d8ccb4 40%,#fff 72%)"></div><span class="btn">Add to Cart</span></article>
  <article class="card" style="left:888px;top:140px"><span class="title">Products Velmo 4</span><span class="price"><s>$130.00</s>$110.00</span><span class="stars">★★★★★</span><span class="sale">SALE</span><div class="photo" role="img" aria-label="Control board with display" style="background:radial-gradient(ellipse at 50% 55%,#4e7a3e,#a8bf96 45%,#fff 76%)"></div><span class="zoom"><svg width="12" height="12" viewBox="0 0 24 24"><circle cx="10" cy="10" r="6" fill="none" stroke="#fff" stroke-width="3"/><path d="M15 15l6 6" stroke="#fff" stroke-width="3"/></svg></span><span class="btn">Add to Cart</span></article>

  <article class="card" style="left:60px;top:560px"><span class="title">Products Velmo 5</span><span class="price"><s>$130.00</s>$110.00</span><span class="stars">★★★★★</span><div class="photo" role="img" aria-label="Embedded circuit board" style="background:radial-gradient(ellipse at 50% 55%,#3f5a30,#9fb08c 45%,#fff 76%)"></div><span class="btn">Add to Cart</span></article>
  <article class="card" style="left:336px;top:560px"><span class="title">Products Velmo 6</span><span class="price"><s>$130.00</s>$110.00</span><span class="stars">★★★★★</span><div class="photo" role="img" aria-label="Starter motor unit" style="background:radial-gradient(ellipse at 50% 55%,#8a6e3e,#cdbb98 45%,#fff 76%)"></div><span class="btn">Add to Cart</span></article>
  <article class="card" style="left:612px;top:560px"><span class="title">Products Velmo 7</span><span class="price"><s>$130.00</s>$110.00</span><span class="stars">★★★★★</span><span class="sale">NEW</span><div class="photo" role="img" aria-label="Linear position sensor" style="background:radial-gradient(ellipse at 50% 55%,#9a9a9a,#d6d6d6 40%,#fff 72%)"></div><span class="btn">Add to Cart</span></article>
  <article class="card" style="left:888px;top:560px"><span class="title">Products Velmo 8</span><span class="price"><s>$130.00</s>$110.00</span><span class="stars">★★★★★</span><div class="photo" role="img" aria-label="Rotary encoder ring" style="background:radial-gradient(circle,#fff 28%,#b8bcc0 44%,#e4e6e8 56%,#fff 72%)"></div><span class="btn">Add to Cart</span></article>
</section>

<section class="abs why">
  <div class="photo" role="img" aria-label="Close-up of an industrial gear mechanism"></div>
  <div class="panel" role="img" aria-label="Olive toned circuit board background"></div>
  <h2>Why we are the best partner<br>for precision systems</h2>
  <ul>
    <li>Over 15 passionate full time engineers</li>
    <li>Over 20 years of know-how in precision automation</li>
    <li>Fast delivery of components and documents to every customer site</li>
  </ul>
  <span class="btn">Download E-Catalog</span>
</section>

<section class="abs start">
  <h2>Get Started With Your Products Order Now</h2>
  <p class="sub">Fast delivery, dedicated engineering support and fair prices.</p>
  <div class="dots"></div>
  <div class="step" style="left:248px"><svg width="54" height="54" viewBox="0 0 24 24"><path fill="#fff" d="M9 2a2 2 0 0 1 2 2v7l5 1.2c1 .3 1.6 1.2 1.4 2.2L16 22H9l-4-6 1.5-1.2L9 17V4z"/></svg></div>
  <div class="step" style="left:548px"><svg width="50" height="50" viewBox="0 0 24 24"><path fill="#fff" d="M6.6 10.8a15 15 0 0 0 6.6 6.6l2.2-2.2c.3-.3.7-.4 1-.2 1.1.4 2.3.6 3.6.6.6 0 1 .4 1 1V20c0 .6-.4 1-1 1A17 17 0 0 1 3 4c0-.6.4-1 1-1h3.5c.6 0 1 .4 1 1 0 1.3.2 2.5.6 3.6.1.3 0 .7-.2 1z"/></svg></div>
  <div class="step" style="left:848px"><svg width="50" height="50" viewBox="0 0 24 24"><rect x="3" y="9" width="18" height="4" fill="#fff"/><rect x="5" y="13" width="14" height="9" fill="#fff"/><rect x="11" y="9" width="2" height="13" fill="#a29a5a"/><path d="M12 9C9 4 5 5 7 8zM12 9c3-5 7-4 5-1z" fill="#fff"/></svg></div>
  <div class="signup"><span class="field"></span><span class="go">Submit</span></div>
</section>

<section class="abs perks">
  <div class="perk dark">
    <svg width="44" height="30" viewBox="0 0 32 22"><rect x="1" y="3" width="18" height="12" fill="#fff"/><path d="M19 7h7l4 5v3H19z" fill="#fff"/><circle cx="8" cy="18" r="3" fill="#fff"/><circle cx="25" cy="18" r="3" fill="#fff"/></svg>
    <div><div class="t">International Delivery</div><div class="s">Over 20 Countries</div></div>
  </div>
  <div class="perk olive">
    <svg width="36" height="36" viewBox="0 0 24 24"><path fill="#fff" d="M9 2a2 2 0 0 1 2 2v7l5 1.2c1 .3 1.6 1.2 1.4 2.2L16 22H9l-4-6 1.5-1.2L9 17z"/></svg>
    <div><div class="t">Click &amp; Collect</div><div class="s">Convenient shipping slots</div></div>
  </div>
  <div class="perk olive">
    <svg width="44" height="30" viewBox="0 0 32 22"><rect x="1" y="3" width="18" height="12" fill="#fff"/><path d="M19 7h7l4 5v3H19z" fill="#fff"/><circle cx="8" cy="18" r="3" fill="#fff"/><circle cx="25" cy="18" r="3" fill="#fff"/></svg>
    <div><div class="t">Free Standard Delivery</div><div class="s">Orders $50 and over</div></div>
  </div>
</section>

<footer class="abs footer">
  <div class="col" style="left:60px">
    <h4>Contact Us</h4>
    <p>Via Campione 14</p>
    <p>CH-6000 Sampleton</p>
    <p>&nbsp;</p>
    <p>+41 (0)00 555 01 23</p>
    <p>info@velmo-example.ch</p>
  </div>
  <div class="col" style="left:360px">
    <h4>Services</h4>
    <ul><li>About Us</li><li>Privacy Policy</li><li>Terms &amp; Conditions</li><li>Best Seller</li><li>Manufactures</li></ul>
  </div>
  <div class="col" style="left:580px">
    <h4>Payment Methods</h4>
    <div class="pay"><span></span><span></span><span></span><span></span></div>
    <div class="label">Shipping Partner</div>
    <div class="pay"><span></span><span></span><span></span><span></span></div>
  </div>
  <div class="col news" style="left:900px">
    <h4>Newsletter !</h4>
    <p>Sign up for our newsletter and get 10% off your next order.</p>
    <div class="field"><i>Enter your email here</i><b></b></div>
    <div class="social"><span></span><span></span><span></span><span></span><span></span></div>
  </div>
</footer>

<div class="abs legal">
  <span class="left">© 2018 Copyright Velmo Sagl · All Rights Reserved</span>
  <span class="right"><span>Privacy &amp; Cookies</span><span>Terms &amp; Conditions</span><span>Accessibility</span><span>Store Directory</span><span>About Us</span></span>
</div>

</body>
</html>
```